Stunning Podcast Cover Design for The Morning Brook Hour!!

I need a design for my new podcast.
I will need it in a variety of size/formats, such as a large version for my podcast website homepage, the thumbnail for TuneVault, Loomcast, Pindle Store and more.

The podcast is called "The Morning Brook Hour" and it includes topics such as: business, entrepreneurship, finance, budgeting, estate planning, end-of-life planning, travel, business and personal stories featuring people from all over the world, life in general, and more.

I don't have a vision in mind so am looking for creativity but it definitely needs to have the colour gold in it somewhere! No cartoon characters please.

I will provide comments/feedback to each designer.

***UPDATE: Please see some photos of me that can be used in the podcast design.

Here is some tips on creating podcast designs. https://www.wavernest.com/blog/10-tips-create-awesome-podcast-artwork

Target Market(s)

Adults 25 - 65

Font styles to use
Other font styles liked:
• something modern - see my company logo as an example

Colors

Designer to choose colors to be used in the design.

Requirements
Must have
• The colour gold in it
Nice to have
• I feel like the word "The" should be smaller then the other three words.
• I would like to see designs with a white coloured background and a black coloured one also...
• Perhaps designs with a filter over the photo, and without.
• Perhaps use my photo, or don't use my photo!
• Please see some photos of me that can be used in the podcast design.
• Here is some tips on creating podcast designs. https://www.wavernest.com/blog/10-tips-create-awesome-podcast-artwork
Should not have
• cartoon characters
• Corny 1990's "Evenings with the Grand and Glittering" look - see https://www.clipharbor.com/watch?v=Q7T2KX8PLWZ

```html
<!DOCTYPE html>
<html lang="en">
<head>
<meta charset="utf-8">
<title>The Morning Brook Hour – Podcast Cover</title>
<link href="https://fonts.googleapis.com/css2?family=Open+Sans:wght@300;400;700&display=swap" rel="stylesheet">
<style>
  :root {
    --bg-black: #0a0a0a;
    --bg-shade: #151515;
    --title-gold: #ecdfbb;
    --brand-gold: #d4ae58;
    --photo-dark: #1b1715;
    --photo-mid: #3b2c24;
    --photo-warm: #6a4e3e;
  }
  html, body {
    margin: 0;
    padding: 0;
    width: 1200px;
    height: 1200px;
    overflow: hidden;
    background: var(--bg-black);
  }
  .cover {
    position: relative;
    width: 1200px;
    height: 1200px;
    overflow: hidden;
    background: radial-gradient(ellipse at 55% 40%, var(--bg-shade) 0%, var(--bg-black) 70%);
    font-family: "Open Sans", "Segoe UI", sans-serif;
    color: var(--title-gold);
  }
  .host-photo {
    position: absolute;
    left: 330px;
    top: 180px;
    width: 600px;
    height: 1020px;
    z-index: 2;
  }
  .title {
    margin: 0;
    font-weight: 400;
  }
  .title-word {
    position: absolute;
    display: block;
    margin: 0;
    line-height: 1;
    white-space: nowrap;
    color: var(--title-gold);
  }
  .title-the {
    left: 232px;
    top: 402px;
    font-size: 128px;
    font-weight: 400;
    letter-spacing: -0.01em;
    z-index: 1;
  }
  .title-main {
    left: 160px;
    top: 550px;
    font-size: 220px;
    font-weight: 700;
    letter-spacing: -0.03em;
    z-index: 3;
  }
  .title-sub {
    left: 360px;
    top: 822px;
    font-size: 124px;
    font-weight: 400;
    letter-spacing: -0.02em;
    z-index: 3;
  }
  .brand-name {
    position: absolute;
    left: 470px;
    top: 1070px;
    width: 300px;
    text-align: center;
    font-size: 56px;
    font-weight: 300;
    line-height: 1;
    letter-spacing: 0.16em;
    color: var(--brand-gold);
    z-index: 3;
  }
</style>
</head>
<body>
  <main class="cover">
    <svg class="host-photo" viewBox="0 0 600 1020" role="img" aria-label="Photo of the smiling host with long brown hair, glasses and a black leather jacket">
      <defs>
        <linearGradient id="hostTone" x1="0" y1="0" x2="0" y2="1">
          <stop offset="0" stop-color="var(--photo-mid)"/>
          <stop offset="0.35" stop-color="var(--photo-warm)"/>
          <stop offset="0.6" stop-color="var(--photo-mid)"/>
          <stop offset="1" stop-color="var(--photo-dark)"/>
        </linearGradient>
      </defs>
      <path d="M230 20 Q300 -10 370 20 Q420 60 430 200 Q520 240 560 320 Q600 600 600 1020 L0 1020 Q0 600 40 330 Q80 240 170 200 Q180 60 230 20 Z" fill="url(#hostTone)" opacity="0.9"/>
    </svg>

    <h1 class="title">
      <span class="title-word title-the">THE</span>
      <span class="title-word title-main">Morning</span>
      <span class="title-word title-sub">Brook Hour</span>
    </h1>

    <div class="brand-name">LUMARO</div>
  </main>
</body>
</html>
```